New Website for Consulting Company

Our company needs a fresh web design to help us drive our business forward. We are a consulting and software provider to Airports, Air Traffic Organizations, Builders and Architects. We specialize in analyzing operations, monitoring noise levels and creating software to improve operations, meet customer requirements and improve public relations.
Additional Info:
- Additional requirements can be found in the Web Design Brief
- Logo and logo branding attached
Target Market(s)
Airlines, Airports, Government Agencies, and Real Estate Developers
Industry/Entity Type
Aviation
Coding
Coded - Design and coding required
Number of Pages Required
2 page
Colors
Designer to choose colors to be used in the design.
Requirements
Must have
- - Create a Wordpress Design (Coded - Design and coding required)
- - Designer must provide full implementation/coding depending on the platform chosen by the client (i.e. Wordpress theme, HTML/CSS, etc.)
- - This is a multi-page site; Supporting pages can be formatted the same, but links need to be in place
- - Colors used must be grey scale, black or match the logo. It is not necessary to use all the colors in our logo
Should not have
- We are not looking for an overly bright site. While our logo has 5 different colors, it is not necessary to use all of them.

```html
<!DOCTYPE html>
<html lang="en">
<head>
<meta charset="utf-8">
<title>Quorvane — Consulting &amp; Software for Airport Traffic Signals</title>
<link rel="stylesheet" href="https://fonts.googleapis.com/css2?family=Questrial&family=Open+Sans:wght@400;600&display=swap">
<style>
  :root {
    --brand-blue: #2a6fa6;
    --brand-blue-dark: #0e2c57;
    --ink: #2b2b2b;
    --ink-soft: #555;
    --muted: #8a8a8a;
    --paper: #ffffff;
    --mist: #f0f0f0;
    --mist-dark: #e4e4e4;
    --hero-top: #3d5f8e;
    --hero-bottom: #1d2b38;
  }
  * { box-sizing: border-box; margin: 0; padding: 0; }
  html, body { width: 1200px; height: 3237px; overflow: hidden; }
  body { font-family: "Questrial", sans-serif; color: var(--ink); background: var(--paper); position: relative; }
  a { color: inherit; text-decoration: none; }
  p { font-family: "Open Sans", sans-serif; }

  .btn {
    display: inline-block; border: 2px solid currentColor; font-family: "Open Sans", sans-serif;
    font-size: 13px; letter-spacing: 1px; text-transform: uppercase;
    padding: 0 26px; height: 42px; line-height: 38px;
  }

  /* Header */
  .site-header { position: absolute; top: 0; left: 0; width: 1200px; height: 104px; background: var(--paper); }
  .brand { position: absolute; left: 142px; top: 30px; display: flex; align-items: center; gap: 10px;
    font-size: 36px; font-weight: 400; color: var(--brand-blue-dark); }
  .brand-dot { width: 14px; height: 14px; border-radius: 50%; background: var(--brand-blue); }
  .main-nav { position: absolute; right: 145px; top: 44px; display: flex; gap: 28px; font-size: 18px; color: var(--ink-soft); }

  /* Hero */
  .hero { position: absolute; top: 104px; left: 0; width: 1200px; height: 556px;
    background: linear-gradient(180deg, var(--hero-top) 0%, #5a7ba2 40%, #2f4050 70%, var(--hero-bottom) 100%); }
  .hero-title { position: absolute; left: 125px; top: 214px; font-size: 42px; line-height: 46px; color: #fff; font-weight: 400; }
  .hero .btn { position: absolute; left: 130px; top: 319px; color: #fff; }
  .hero-dots { position: absolute; left: 555px; top: 518px; display: flex; gap: 10px; }
  .hero-dots span { width: 12px; height: 12px; border-radius: 50%; background: #fff; }
  .hero-dots span:first-child { background: transparent; border: 2px solid #fff; }

  /* What we do */
  .what-we-do { position: absolute; top: 660px; left: 0; width: 1200px; height: 428px; background: var(--mist); }
  .section-title { font-size: 32px; font-weight: 400; color: var(--ink-soft); }
  .what-we-do .section-title { position: absolute; left: 145px; top: 78px; }
  .what-we-do .copy { position: absolute; left: 147px; top: 136px; width: 400px; font-size: 13px; line-height: 22px; color: var(--muted); }
  .what-we-do .copy p + p { margin-top: 12px; }
  .what-we-do .btn { position: absolute; left: 147px; top: 298px; color: var(--ink); }
  .what-we-do .illustration { position: absolute; left: 529px; top: 20px; width: 647px; height: 377px;
    background: linear-gradient(160deg, #e9ecef 0%, #c9d2da 45%, #9fb0bd 70%, #e6e9ec 100%);
    clip-path: polygon(5% 70%, 60% 10%, 100% 35%, 45% 100%); }

  /* Expertise */
  .expertise { position: absolute; top: 1088px; left: 0; width: 1200px; height: 401px; background: var(--brand-blue); color: #fff; text-align: center; }
  .expertise .section-title { color: #fff; font-size: 30px; position: absolute; top: 50px; width: 100%; }
  .expertise .rule { position: absolute; left: 585px; top: 96px; width: 30px; height: 2px; background: #fff; }
  .expertise-item { position: absolute; top: 129px; width: 240px; }
  .expertise-item .icon { width: 112px; height: 112px; margin: 0 auto; display: block; }
  .expertise-item h3 { font-weight: 400; font-size: 21px; margin-top: 18px; }
  .expertise-item p { font-size: 11px; line-height: 20px; margin: 6px auto 0; width: 190px; opacity: .9; }

  /* Analyzing */
  .analyzing { position: absolute; top: 1489px; left: 0; width: 1200px; height: 471px; background: var(--paper); overflow: hidden; }
  .analyzing .diagonal { position: absolute; inset: 0; background: var(--mist-dark); clip-path: polygon(0 0, 612px 0, 0 100%); }
  .analyzing .screen { position: absolute; left: 97px; top: 97px; width: 490px; height: 283px;
    background: radial-gradient(circle at 50% 50%, #2a6a9c 0%, #173d63 45%, #0d1f33 100%);
    border-radius: 10px 10px 4px 4px; }
  .analyzing .section-title { position: absolute; left: 615px; top: 122px; color: var(--brand-blue); font-size: 30px; }
  .analyzing .copy { position: absolute; left: 615px; top: 166px; width: 450px; font-size: 13px; line-height: 22px; color: var(--muted); }
  .analyzing .copy p + p { margin-top: 10px; }
  .analyzing .btn { position: absolute; left: 615px; top: 317px; color: var(--brand-blue); }

  /* Feature panels */
  .feature { position: absolute; top: 1960px; width: 598px; height: 388px; color: #fff; }
  .feature.noise { left: 0; background: linear-gradient(180deg, #6d8aa8 0%, #44525e 50%, #2b2f33 100%); }
  .feature.visual { left: 602px; background: var(--brand-blue-dark); }
  .feature h3 { position: absolute; left: 149px; top: 186px; font-size: 29px; font-weight: 400; }
  .feature.visual h3 { left: 69px; }
  .feature p { position: absolute; left: 149px; top: 226px; width: 380px; font-size: 12px; line-height: 20px; }
  .feature.visual p { left: 69px; }
  .feature .btn { position: absolute; left: 149px; top: 289px; color: #fff; }
  .feature.visual .btn { left: 69px; }

  /* Blog */
  .blog { position: absolute; top: 2348px; left: 0; width: 1200px; height: 501px; background: var(--mist); }
  .blog .section-title { position: absolute; left: 134px; top: 50px; font-size: 30px; }
  .post { position: absolute; top: 101px; width: 298px; height: 346px; background: var(--paper); }
  .post .thumb { height: 177px; }
  .post h4 { font-family: "Open Sans", sans-serif; font-weight: 600; font-size: 13px; line-height: 20px; margin: 24px 30px 0; color: var(--ink); }
  .post p { font-size: 11px; line-height: 18px; margin: 8px 30px 0; color: var(--muted); }
  .post a { display: block; margin: 10px 30px 0; font-family: "Open Sans", sans-serif; font-size: 11px; color: var(--brand-blue); text-transform: uppercase; }

  /* Footer */
  .site-footer { position: absolute; top: 2849px; left: 0; width: 1200px; height: 323px; background: var(--paper); }
  .footer-col { position: absolute; top: 70px; }
  .footer-col h5 { font-size: 20px; font-weight: 400; color: var(--brand-blue); margin-bottom: 6px; }
  .footer-col li { list-style: none; font-family: "Open Sans", sans-serif; font-size: 14px; line-height: 27px; color: var(--ink-soft); }
  .footer-brand { position: absolute; left: 734px; top: 92px; display: flex; align-items: center; gap: 10px; font-size: 36px; color: var(--brand-blue-dark); }
  .social { position: absolute; left: 520px; top: 225px; display: flex; gap: 12px; }
  .social span { width: 32px; height: 32px; border: 2px solid var(--brand-blue); border-radius: 50%; }
  .legal { position: absolute; top: 3172px; left: 0; width: 1200px; height: 65px; background: var(--mist-dark);
    text-align: center; line-height: 65px; font-family: "Open Sans", sans-serif; font-size: 12px; color: var(--muted); }
</style>
</head>
<body>

<header class="site-header">
  <a class="brand" href="#"><span class="brand-dot"></span>Quorvane</a>
  <nav class="main-nav">
    <a href="#">Airports</a><a href="#">Airspace</a><a href="#">Emissions</a><a href="#">Acoustics</a>
    <a href="#">Visualization</a><a href="#">About</a><a href="#">Contact</a>
  </nav>
</header>

<section class="hero" role="img" aria-label="Airliner landing over a lit runway at dusk">
  <h1 class="hero-title">Consulting &amp; Software for<br>Airport Traffic Signals</h1>
  <a class="btn" href="#">Learn More</a>
  <div class="hero-dots"><span></span><span></span><span></span><span></span></div>
</section>

<section class="what-we-do">
  <h2 class="section-title">What We Do</h2>
  <div class="copy">
    <p>Praesent elementum elit at tellus nec ultricies sit amet porttitor mattis enim In massa libero interdum nec interdum vel blandit sed nulla In ullamcorper</p>
    <p>neque mi consectetuer mi a ultricies massa est sed tortor at ipsum Proin orci odio commodo</p>
  </div>
  <a class="btn" href="#">Learn More</a>
  <div class="illustration" role="img" aria-label="Isometric illustration of an airport terminal with control tower and parked airliners"></div>
</section>

<section class="expertise">
  <h2 class="section-title">Areas of Expertise</h2>
  <div class="rule"></div>

  <div class="expertise-item" style="left:120px">
    <svg class="icon" viewBox="0 0 112 112" fill="none" stroke="#fff" stroke-width="1.5">
      <circle cx="56" cy="56" r="54"/><circle cx="56" cy="56" r="46" opacity=".5"/>
      <path d="M38 72h36M42 72V52h10v20M52 58h20v14M44 46h6l-3 6M56 48l14-4" />
    </svg>
    <h3>Airports</h3>
    <p>sociosqu ad litora torquent per conubia nostra per inceptos hyme</p>
  </div>

  <div class="expertise-item" style="left:357px">
    <svg class="icon" viewBox="0 0 112 112" fill="none" stroke="#fff" stroke-width="1.5">
      <circle cx="56" cy="56" r="54"/><circle cx="56" cy="56" r="46" opacity=".5"/>
      <rect x="36" y="38" width="40" height="34"/><path d="M36 45h40M50 54l12 10M62 54l-12 10"/>
    </svg>
    <h3>Software</h3>
    <p>sociosqu ad litora torquent per conubia nostra per inceptos hyme</p>
  </div>

  <div class="expertise-item" style="left:594px">
    <svg class="icon" viewBox="0 0 112 112" fill="none" stroke="#fff" stroke-width="1.5">
      <circle cx="56" cy="56" r="54"/><circle cx="56" cy="56" r="46" opacity=".5"/>
      <g fill="#fff" stroke="none">
        <circle cx="44" cy="44" r="2"/><circle cx="52" cy="44" r="2"/><circle cx="60" cy="44" r="2"/><circle cx="68" cy="44" r="2"/>
        <circle cx="40" cy="52" r="2"/><circle cx="48" cy="52" r="2"/><circle cx="56" cy="52" r="2"/><circle cx="64" cy="52" r="2"/><circle cx="72" cy="52" r="2"/>
        <circle cx="44" cy="60" r="2"/><circle cx="52" cy="60" r="2"/><circle cx="60" cy="60" r="2"/><circle cx="68" cy="60" r="2"/>
        <circle cx="48" cy="68" r="2"/><circle cx="56" cy="68" r="2"/><circle cx="64" cy="68" r="2"/>
      </g>
    </svg>
    <h3>Noise &amp; Emissions</h3>
    <p>sociosqu ad litora torquent per conubia nostra per inceptos hyme</p>
  </div>

  <div class="expertise-item" style="left:842px">
    <svg class="icon" viewBox="0 0 112 112" fill="none" stroke="#fff" stroke-width="1.5">
      <circle cx="56" cy="56" r="54"/><circle cx="56" cy="56" r="46" opacity=".5"/>
      <g fill="#fff" stroke="none"><rect x="40" y="56" width="7" height="16"/><rect x="51" y="48" width="7" height="24"/><rect x="62" y="40" width="7" height="32"/></g>
    </svg>
    <h3>Visualization</h3>
    <p>sociosqu ad litora torquent per conubia nostra per inceptos hyme</p>
  </div>
</section>

<section class="analyzing">
  <div class="diagonal"></div>
  <div class="screen" role="img" aria-label="Laptop showing an air traffic radar display"></div>
  <h2 class="section-title">Analyzing Operations</h2>
  <div class="copy">
    <p>Praesent elementum elit at tellus nec ultricies sit amet porttitor mattis enim In massa libero interdum nec interdum vel blandit sed nulla In ullamcorper est eget tempor cursus</p>
    <p>neque mi consectetuer mi a ultricies massa est sed nisl Class aptent taciti sociosqu ad litora</p>
  </div>
  <a class="btn" href="#">Learn More</a>
</section>

<section class="feature noise" role="img" aria-label="Operators at screens inside an airport control tower">
  <h3>Monitoring Noise Levels</h3>
  <p>tortor at ipsum Proin orci odio commodo ac gravida non tristique vel tellus Pellentesque nibh libero ultricies eu</p>
  <a class="btn" href="#">Learn More</a>
</section>

<section class="feature visual" role="img" aria-label="Wireframe drawing of a tall building on deep blue">
  <h3>Visualization &amp; Architect</h3>
  <p>tortor at ipsum Proin orci odio commodo ac gravida non tristique vel tellus Pellentesque nibh libero ultricies</p>
  <a class="btn" href="#">Learn More</a>
</section>

<section class="blog">
  <h2 class="section-title">Blogs &amp; News</h2>
  <article class="post" style="left:134px">
    <div class="thumb" role="img" aria-label="Airport apron at night" style="background:linear-gradient(180deg,#4f78a8,#263a52)"></div>
    <h4>Aortor at ipsum Proin orci odio commodo ac gravida non</h4>
    <p>Praesent elementum elit at tellus nec ultricies sit amet porttitor mattis enim</p>
    <a href="#">Learn More</a>
  </article>
  <article class="post" style="left:447px">
    <div class="thumb" role="img" aria-label="Controller at a radar workstation" style="background:linear-gradient(180deg,#8a96a2,#3a4550)"></div>
    <h4>Aortor at ipsum Proin orci odio commodo ac gravida non</h4>
    <p>Praesent elementum elit at tellus nec ultricies sit amet porttitor mattis enim</p>
    <a href="#">Learn More</a>
  </article>
  <article class="post" style="left:762px">
    <div class="thumb" role="img" aria-label="Flight path network graphic on dark background" style="background:linear-gradient(180deg,#2a2f36,#14171b)"></div>
    <h4>Aortor at ipsum Proin orci odio commodo ac gravida non</h4>
    <p>Praesent elementum elit at tellus nec ultricies sit amet porttitor mattis enim</p>
    <a href="#">Learn More</a>
  </article>
</section>

<footer class="site-footer">
  <div class="footer-col" style="left:145px">
    <h5>Company</h5>
    <ul><li>Home</li><li>About</li><li>Airspace</li><li>Emissions</li><li>Acoustics</li></ul>
  </div>
  <div class="footer-col" style="left:328px">
    <h5>Resources</h5>
    <ul><li>Visualization</li><li>Blogs</li><li>Contact</li><li>Services</li><li>News</li></ul>
  </div>
  <div class="footer-col" style="left:524px">
    <h5>Areas</h5>
    <ul><li>Airports</li><li>Software</li><li>Noise &amp; Emissions</li><li>Visualization</li></ul>
  </div>
  <div class="footer-brand"><span class="brand-dot"></span>Quorvane</div>
  <div class="social"><span aria-label="Social profile"></span><span aria-label="Social profile"></span></div>
</footer>

<div class="legal">© 2017 Company Name. All right reserved</div>

</body>
</html>
```